Trade show banner design

We need an 8 x 2.5' and a 6 x 2.5' banner for trade shows. We would like you to use the last book cover design you submitted with the woman on the right of the banner using the catchphrase underneath and the couple on the left of the banner with the catchphrase underneath. We prefer the font under the couple, so please use this for both. In the middle at the top will be the company logo and www.velmorapages.com with our phone numbers underneath that. If you think the logo would look nicer in the middle please feel free to play with the balance.
Also, the Velmora Pages will not be necessary above the woman's head.
THANK YOU!!!!!!!!
717-555-0172 and 844-4VELMORA.

```html
<!DOCTYPE html>
<html lang="en">
<head>
<meta charset="utf-8">
<title>Velmora Pages – Trade Show Banner 8 x 2.5 ft</title>
<link rel="stylesheet" href="https://fonts.googleapis.com/css2?family=Cormorant+Garamond:ital,wght@0,600;1,500;1,600;1,700&display=swap">
<style>
  :root {
    --page: #ffffff;
    --banner: #f9a98a;
    --ink: #111111;
    --brand: #8a3a12;
    --band-light: #fff3ee;
    --band-pink: #f6a6a0;
    --rule: #b9a9a4;
    --flourish: #9c8f8c;
    --sunset-top: #f6e9a8;
    --sunset-mid: #e4b05a;
    --sunset-dark: #2a140c;
    --study-light: #d8c3a8;
    --study-dark: #3b2418;
    --oval-glow: #ffe7d8;
  }
  * { margin: 0; padding: 0; box-sizing: border-box; }
  html, body { width: 1200px; height: 900px; overflow: hidden; background: var(--page); }
  body { position: relative; font-family: "Cormorant Garamond", Georgia, serif; color: var(--ink); }

  .size-label {
    position: absolute; top: 165px; left: 0; width: 1150px; text-align: center;
    font-style: italic; font-weight: 500; font-size: 44px; letter-spacing: 1px;
  }

  .banner {
    position: absolute; left: 0; top: 388px; width: 1200px; height: 374px;
    background: var(--banner); overflow: hidden;
  }
  .banner > * { position: absolute; }

  .corner-flourish { width: 60px; height: 36px; top: 6px; background: var(--flourish); opacity: .55; border-radius: 0 0 40px 0; }
  .corner-flourish.left { left: 6px; }
  .corner-flourish.right { right: 8px; border-radius: 0 0 0 40px; }

  .photo { left: 0; top: 0; }

  .web-address { left: 218px; top: 8px; font-style: italic; font-weight: 700; font-size: 26px; letter-spacing: 1px; }
  .phones { left: 737px; top: 10px; font-style: italic; font-weight: 600; font-size: 30px; line-height: 27px; letter-spacing: 1px; }

  .logo { left: 430px; top: 70px; width: 340px; height: 90px; display: flex; align-items: center; justify-content: center; gap: 14px; }
  .logo-dot { width: 18px; height: 18px; border-radius: 50%; background: var(--brand); }
  .logo-name { font-weight: 600; font-size: 42px; color: var(--brand); letter-spacing: 1px; }

  .title-band {
    left: 258px; top: 200px; width: 692px; height: 112px;
    background: linear-gradient(to bottom, var(--band-light) 0%, var(--band-pink) 100%);
  }
  .title { left: 280px; top: 190px; white-space: nowrap; font-style: italic; font-weight: 500; }
  .title .small { font-size: 64px; letter-spacing: 2px; }
  .title .big { font-size: 118px; margin-left: 8px; }

  .tagline { text-align: center; font-style: italic; font-weight: 600; letter-spacing: .8px; line-height: 22px; }
  .tagline.left { left: 20px; top: 326px; width: 238px; font-size: 21px; }
  .tagline.right { left: 892px; top: 334px; width: 304px; font-size: 19px; line-height: 19px; }
</style>
</head>
<body>
  <p class="size-label">8 feet x 2.5 feet</p>

  <section class="banner">
    <div class="corner-flourish left" role="img" aria-label="Decorative corner scroll"></div>
    <div class="corner-flourish right" role="img" aria-label="Decorative corner scroll"></div>

    <svg class="photo" width="1200" height="374" viewBox="0 0 1200 374">
      <defs>
        <linearGradient id="sunset" x1="0" y1="0" x2="0" y2="1">
          <stop offset="0" stop-color="var(--sunset-top)"/>
          <stop offset=".45" stop-color="var(--sunset-mid)"/>
          <stop offset=".6" stop-color="var(--sunset-dark)"/>
          <stop offset="1" stop-color="var(--sunset-dark)"/>
        </linearGradient>
        <linearGradient id="study" x1="0" y1="0" x2="1" y2="1">
          <stop offset="0" stop-color="var(--study-dark)"/>
          <stop offset=".6" stop-color="#7a5a44"/>
          <stop offset="1" stop-color="var(--study-light)"/>
        </linearGradient>
      </defs>
      <ellipse cx="143" cy="175" rx="114" ry="157" fill="var(--oval-glow)"/>
      <ellipse cx="143" cy="175" rx="110" ry="153" fill="url(#sunset)" role="img" aria-label="Photo of an older couple walking by the water at sunset"/>
      <ellipse cx="1060" cy="162" rx="104" ry="142" fill="var(--oval-glow)"/>
      <ellipse cx="1060" cy="162" rx="100" ry="138" fill="url(#study)" role="img" aria-label="Photo of an elderly woman writing at a wooden desk"/>
      <line x1="305" y1="334" x2="862" y2="334" stroke="var(--rule)" stroke-width="2"/>
      <rect x="395" y="323" width="380" height="22" rx="11" fill="#f3c2b2" role="img" aria-label="Decorative scroll ornament"/>
    </svg>

    <p class="web-address">www.velmorapages.com</p>
    <p class="phones">717-555-0172 and<br>844-4VELMORA</p>

    <div class="logo">
      <span class="logo-dot"></span>
      <span class="logo-name">Velmora Pages</span>
    </div>

    <div class="title-band"></div>
    <h1 class="title"><span class="small">Velmora</span><span class="big">Pages</span></h1>

    <p class="tagline left">"When a genealogy<br>doesn't say enough"</p>
    <p class="tagline right">Every life legacy is a gift to be<br>treasured by the next generation</p>
  </section>
</body>
</html>
```